Development of musical artist Torvan Quell's Website

I need a website designed for a reggae musical artist by the name of Torvan Quell. The site should be representative of a Reggae artist from Jamaica that has a Caribbean appeal but also attractive to global audiences. The website should be responsive for all devices (desktop, laptop, mobile). It should be optimized for SEO purposes. Icons for Instagram, Facebook, Twitter, YouTube should be included. The sections of the website should be as follows: Home, Media, News, Bio, Join, Contact. The 'Join' section should be a form for database collection to the fan club. I would like to easily be able to dump this database in an excel or .csv file at any given time. The 'Media' section should be able to showcase video thumbnails and allow persons to play videos through the site and the videos will be fed from YouTube. The 'News' section will be for announcements and or new releases where the artist is mentioned. The site should also be built in such a way that analytics can be easily implemented. This website should be the main call to action for this artist moving forward. I would also like the website to have a easy to use CMS platform (Wordpress perhaps). The URL for the website will be torvanquellstar.example. Here are the links for some of the social media pages:
YouTube - https://www.videohub.example/user/TorvanQuell
Instagram - https://www.snapgram.example/torvanquell/
A good website to refer to from a design perspective is https://maldoreef.example/

Target Market(s)

Reggae and Pop music fans

Industry/Entity Type

Artists

Coding

Coded - Design and coding required

Number of Pages Required

5+ page

Font styles to use
Sans Serif

Requirements
Must have
• Great design
Nice to have
• Parallax technology

```html
<!DOCTYPE html>
<html lang="en">
<head>
<meta charset="utf-8">
<title>Torvan Quell — Official Site</title>
<link href="https://fonts.googleapis.com/css2?family=Exo+2:wght@400;500;600;700;800&family=Orbitron:wght@700;800;900&display=swap" rel="stylesheet">
<style>
:root{
  --red:#e0142a;
  --red-deep:#c20d20;
  --black:#0b0b0b;
  --ink:#2a2a2a;
  --grey:#e6e6e6;
  --white:#ffffff;
  --text:#4a4a4a;
}
*{box-sizing:border-box;margin:0;padding:0}
html,body{width:1200px;height:4276px;overflow:hidden}
body{position:relative;background:var(--white);font-family:"Exo 2",sans-serif;color:var(--text)}
.abs{position:absolute}
a{color:inherit;text-decoration:none}

/* header */
.site-header{left:0;top:0;width:1200px;height:103px;background:var(--black);border-top:8px solid var(--red);z-index:10}
.brand{left:86px;top:32px;font-weight:800;font-size:24px;color:var(--white);letter-spacing:1px;display:flex;align-items:center;gap:10px}
.brand-dot{width:14px;height:14px;border-radius:50%;background:var(--red)}
.main-nav{top:44px;left:0;width:1200px;height:20px}
.main-nav a{position:absolute;transform:translateX(-50%);color:var(--white);font-size:16px;font-weight:500;white-space:nowrap}
.social{display:flex;gap:22px}
.social span{width:16px;height:16px;border-radius:50%;background:var(--white);display:block}
.header-social{left:990px;top:45px}

/* hero */
.hero{left:0;top:103px;width:1200px;height:604px;background:linear-gradient(90deg,#0d0a08 0%,#1a110c 55%,#2a1a10 100%);clip-path:polygon(0 0,100% 0,100% 84.4%,0 100%);z-index:3}
.hero-photo{left:640px;top:0;width:420px;height:604px;background:radial-gradient(ellipse at 55% 45%,#5b3a24 0%,#38231a 45%,rgba(30,18,12,0) 75%)}
.hero-title{left:232px;top:196px;font-weight:800;font-size:34px;color:var(--white);letter-spacing:1px;font-style:normal}
.hero-text{left:234px;top:252px;width:400px;font-size:17px;line-height:36px;color:#e8e8e8}
.btn-outline{display:inline-block;border:2px solid var(--red);border-radius:22px;font-size:16px;text-transform:uppercase;padding:8px 22px}
.hero-btn{left:228px;top:340px;color:var(--white)}
.chevron{top:275px}

/* sections */
.section-title{font-family:"Orbitron",sans-serif;font-weight:900;color:var(--red);font-size:26px;letter-spacing:2px;text-align:center;width:1200px;left:0;z-index:4}
.media{left:0;top:613px;width:1200px;height:542px;background:var(--grey);z-index:1}
.media-item{z-index:4}
.thumb{width:332px;height:214px}
.play{width:40px;height:28px;border-radius:7px;background:var(--red);display:flex;align-items:center;justify-content:center}
.play::after{content:"";border-left:11px solid #fff;border-top:7px solid transparent;border-bottom:7px solid transparent}
.thumb-caption{width:300px;font-size:13px;font-weight:700;color:var(--ink);line-height:20px;text-transform:uppercase}

.news-banner{left:0;top:1155px;width:1200px;height:560px;background:linear-gradient(180deg,#5f7c9a 0%,#7d97b0 40%,#a3b7c7 100%);z-index:1}
.news-photo{left:560px;top:1155px;width:560px;height:560px;background:radial-gradient(ellipse at 50% 55%,#3f3228 0%,#5c5048 35%,rgba(120,140,160,0) 72%);z-index:2}
.news-banner-title{left:116px;top:1363px;font-family:"Orbitron",sans-serif;font-weight:800;font-size:24px;line-height:36px;color:var(--white);letter-spacing:2px;z-index:4}
.news-red{left:0;top:1582px;width:1200px;height:712px;background:var(--red);clip-path:polygon(0 0,100% 16%,100% 100%,0 100%);z-index:3}
.news-el{z-index:4}
.news-item-img{left:74px;width:183px;height:122px}
.date{position:absolute;left:20px;bottom:14px;font-size:13px;font-weight:700;color:var(--white)}
.news-item-text{left:271px;width:300px;color:var(--white)}
.news-item-text h3{font-size:18px;font-weight:500;line-height:22px;text-transform:uppercase}
.news-item-text p{font-size:13px;line-height:18px;margin-top:6px}
.read-more{font-size:13px;font-weight:700;margin-top:8px;display:block}
.feature-img{left:613px;top:1776px;width:513px;height:270px;background:linear-gradient(135deg,#3a0d2a 0%,#7a1438 45%,#b01b28 75%,#3a0a14 100%)}
.feature-text{left:613px;top:2068px;width:513px;color:var(--white)}
.feature-text h3{font-size:18px;font-weight:500;text-transform:uppercase}
.feature-text p{font-size:13px;line-height:19px;margin-top:8px}

/* about */
.about{left:0;top:2294px;width:1200px;height:565px;background:linear-gradient(90deg,#ededed 0%,#e4e4e4 100%);z-index:1}
.about-photo{left:440px;top:2294px;width:760px;height:565px;background:linear-gradient(90deg,rgba(228,228,228,0) 0%,#bdbdbd 35%,#6e6460 62%,#d8d8d8 100%);z-index:2}
.about-el{z-index:4}
.about-title{left:535px;top:2346px;width:auto;text-align:left}
.about-text{left:100px;top:2452px;width:400px;font-size:16px;line-height:33px;color:#555}
.about-btn{left:100px;top:2646px;color:var(--red)}

/* join */
.join{left:0;top:2859px;width:1200px;height:675px;background:linear-gradient(160deg,#d4101f 0%,#c60c1c 50%,#b70a18 100%);clip-path:polygon(0 0,100% 0,100% 89.5%,0 100%);z-index:3}
.join-title{top:2975px;color:var(--white)}
.field{border:2px solid #f2c4c8;border-radius:3px;height:57px;color:var(--white);font-size:15px;padding:18px 22px;z-index:4}
.submit{left:462px;top:3320px;width:199px;height:58px;background:var(--black);color:var(--white);font-size:18px;font-weight:600;display:flex;align-items:center;justify-content:center;z-index:4}

/* contact */
.contact-photo{left:560px;top:3480px;width:560px;height:553px;background:radial-gradient(ellipse at 50% 40%,#d9d9d9 0%,#ececec 45%,rgba(255,255,255,0) 75%);z-index:1}
.contact-title{top:3600px;color:var(--black)}
.contact-col{width:360px;text-align:center;z-index:4}
.contact-col h4{color:var(--red);font-size:22px;font-weight:700;margin-top:18px}
.contact-col p{font-size:20px;font-weight:600;color:#555;line-height:40px;margin-top:6px}

/* footer */
.site-footer{left:0;top:4033px;width:1200px;height:243px;background:var(--black);z-index:5}
.footer-el{z-index:6}
.footer-nav{top:4114px;left:0;width:1200px}
.footer-nav a{position:absolute;transform:translateX(-50%);color:var(--white);font-size:15px}
.footer-social{left:488px;top:4162px}
.footer-social span{width:13px;height:13px}
.copyright{left:0;top:4202px;width:1200px;text-align:center;font-size:13px;color:var(--white)}
</style>
</head>
<body>

<header class="site-header abs">
  <a class="brand abs" href="#"><span>TORVAN QUELL!</span><span class="brand-dot"></span></a>
  <nav class="main-nav abs">
    <a href="#" style="left:467px">HOME</a>
    <a href="#" style="left:556px">MEDIA</a>
    <a href="#" style="left:644px">NEWS</a>
    <a href="#" style="left:724px">BIO</a>
    <a href="#" style="left:792px">JOIN</a>
    <a href="#" style="left:895px">CONTACT US</a>
  </nav>
  <div class="social header-social abs">
    <span aria-label="Social link 1"></span><span aria-label="Social link 2"></span><span aria-label="Social link 3"></span><span aria-label="Video channel"></span>
  </div>
</header>

<section class="hero abs">
  <div class="hero-photo abs" role="img" aria-label="Portrait of Torvan Quell in an open shirt and chain"></div>
  <h1 class="hero-title abs">TORVAN QUELL!</h1>
  <p class="hero-text abs">Sed ut perspiciatis unde omnis iste natus error sit voluptatem accusantium...</p>
  <a class="btn-outline hero-btn abs" href="#">Read More</a>
  <svg class="chevron abs" style="left:70px" width="20" height="30" viewBox="0 0 20 30"><path d="M16 3 L5 15 L16 27" stroke="#fff" stroke-width="5" fill="none"/></svg>
  <svg class="chevron abs" style="left:1110px" width="20" height="30" viewBox="0 0 20 30"><path d="M4 3 L15 15 L4 27" stroke="#fff" stroke-width="5" fill="none"/></svg>
</section>

<section class="media abs"></section>
<h2 class="section-title abs" style="top:715px">MEDIA</h2>
<div class="thumb media-item abs" style="left:74px;top:795px;background:linear-gradient(135deg,#5a1a14,#b8452a 50%,#3a1610)" role="img" aria-label="Video still of three artists in a studio"></div>
<div class="thumb media-item abs" style="left:433px;top:795px;background:linear-gradient(180deg,#9ab6c8,#d9d2c4 55%,#6a5446)" role="img" aria-label="Video still of two artists on a beach"></div>
<div class="play media-item abs" style="left:580px;top:888px"></div>
<div class="thumb media-item abs" style="left:795px;top:795px;background:linear-gradient(135deg,#2c2a24,#d7b21e 55%,#7a3a20)" role="img" aria-label="Video still of artists at a street party"></div>
<div class="play media-item abs" style="left:942px;top:888px"></div>
<p class="thumb-caption media-item abs" style="left:96px;top:1026px">Sed ut perspiciatis unde omnis iste natus error sit voluptatem</p>
<p class="thumb-caption media-item abs" style="left:460px;top:1026px">Sed ut perspiciatis unde omnis iste natus error sit voluptatem</p>
<p class="thumb-caption media-item abs" style="left:820px;top:1026px">Sed ut perspiciatis unde omnis iste natus error sit voluptatem</p>

<section class="news-banner abs"></section>
<div class="news-photo abs" role="img" aria-label="Torvan Quell in sunglasses against a blue sky"></div>
<h2 class="section-title abs" style="top:1220px;color:#fff">NEWS</h2>
<p class="news-banner-title abs">ANNOUNCEMENTS &amp;<br>NEW RELEASES</p>

<section class="news-red abs"></section>
<div class="news-item-img news-el abs" style="top:1773px;background:linear-gradient(135deg,#3a2218,#8a5a3a)" role="img" aria-label="News photo of a singer"><span class="date">JAN 18, 2018</span></div>
<div class="news-item-text news-el abs" style="top:1768px"><h3>Sunrise Riddim - Kayo and the Tide</h3><p>Lorem ipsum dolor sit amet, consectetur adipiscing elit. Integer cursus.</p><span class="read-more">READ MORE »</span></div>
<div class="news-item-img news-el abs" style="top:1930px;background:linear-gradient(135deg,#2a1d2a,#6a4a6a)" role="img" aria-label="News photo of an artist"><span class="date">JAN 18, 2018</span></div>
<div class="news-item-text news-el abs" style="top:1922px"><h3>Sunrise Riddim - Kayo and the Tide</h3><p>Lorem ipsum dolor sit amet, consectetur adipiscing elit. Integer cursus.</p><span class="read-more">READ MORE »</span></div>
<div class="news-item-img news-el abs" style="top:2081px;background:linear-gradient(135deg,#5a1a14,#b8452a 55%,#3a1610)" role="img" aria-label="News photo of three artists in a studio"><span class="date">JAN 18, 2018</span></div>
<div class="news-item-text news-el abs" style="top:2076px"><h3>Sunrise Riddim - Kayo and the Tide</h3><p>Lorem ipsum dolor sit amet, consectetur adipiscing elit. Integer cursus.</p><span class="read-more">READ MORE »</span></div>
<div class="feature-img news-el abs" role="img" aria-label="Dancer performing on a stage under red lights"><span class="date" style="left:40px;bottom:30px">JAN 18, 2018</span></div>
<div class="feature-text news-el abs"><h3>Ocean Fire - Torvan Quell / Dax Meridian - Part 1</h3><p>Lorem ipsum dolor sit amet, consectetur adipiscing elit. Integer cursus pretium libero ac maximus fermentum malesuada ligula non fringilla maximus ac magna quis, suscipit commodo urna...</p><span class="read-more">READ MORE »</span></div>

<section class="about abs"></section>
<div class="about-photo abs" role="img" aria-label="Close portrait of Torvan Quell in a striped shirt"></div>
<h2 class="section-title about-title abs">ABOUT</h2>
<p class="about-text about-el abs">Sed ut perspiciatis unde omnis iste natus error sit voluptatem accusantium doloremque laudantium, totam rem aperiam, eaque ipsa quae ab illo inventore veritatis et quasi architecto beatae vitae dicta sunt explicabo. Nemo enim ipsam voluptatem...</p>
<a class="btn-outline about-btn about-el abs" href="#">Read More</a>

<section class="join abs"></section>
<h2 class="section-title join-title abs">JOIN</h2>
<form>
  <div class="field abs" style="left:117px;top:3050px;width:439px">First Name</div>
  <div class="field abs" style="left:567px;top:3050px;width:439px">Last Name</div>
  <div class="field abs" style="left:117px;top:3115px;width:439px">Email address</div>
  <div class="field abs" style="left:567px;top:3115px;width:439px">Phone Number</div>
  <div class="field abs" style="left:117px;top:3184px;width:889px;height:122px">Type Message</div>
  <div class="submit abs">SUBMIT</div>
</form>

<div class="contact-photo abs" role="img" aria-label="Faded portrait of Torvan Quell"></div>
<h2 class="section-title contact-title abs">CONTACT</h2>
<div class="contact-col abs" style="left:31px;top:3730px">
  <svg width="52" height="74" viewBox="0 0 52 74"><path d="M26 4 C13 4 4 14 4 26 C4 42 26 70 26 70 C26 70 48 42 48 26 C48 14 39 4 26 4 Z" fill="none" stroke="#e0142a" stroke-width="4"/><circle cx="26" cy="26" r="8" fill="none" stroke="#e0142a" stroke-width="4"/></svg>
  <h4>ADDRESS</h4><p>42 HARBOR LANE SUITE 4<br>KINGSTON 20418 JM</p>
</div>
<div class="contact-col abs" style="left:376px;top:3730px">
  <svg width="74" height="74" viewBox="0 0 74 74"><path d="M14 6 L26 6 L31 22 L23 28 C27 38 36 47 46 51 L52 43 L68 48 L68 60 C68 64 64 68 60 68 C30 66 8 44 6 14 C6 10 10 6 14 6 Z" fill="none" stroke="#e0142a" stroke-width="4" stroke-linejoin="round"/></svg>
  <h4>PHONE</h4><p>555.010.7391</p>
</div>
<div class="contact-col abs" style="left:715px;top:3730px">
  <svg width="80" height="74" viewBox="0 0 80 74"><rect x="4" y="14" width="72" height="50" fill="none" stroke="#e0142a" stroke-width="4"/><path d="M4 14 L40 42 L76 14" fill="none" stroke="#e0142a" stroke-width="4"/></svg>
  <h4>EMAIL</h4><p>INFO@TQSTAR.EXAMPLE</p>
</div>

<footer class="site-footer abs"></footer>
<nav class="footer-nav footer-el abs">
  <a href="#" style="left:373px">HOME</a>
  <a href="#" style="left:462px">MEDIA</a>
  <a href="#" style="left:550px">NEWS</a>
  <a href="#" style="left:627px">BIO</a>
  <a href="#" style="left:687px">JOIN</a>
  <a href="#" style="left:801px">CONTACT US</a>
</nav>
<div class="social footer-social footer-el abs">
  <span aria-label="Social link 1"></span><span aria-label="Social link 2"></span><span aria-label="News feed"></span><span aria-label="Social link 3"></span><span aria-label="Social link 4"></span>
</div>
<p class="copyright footer-el abs">© 2019 | www.torvanquellstar.example</p>

</body>
</html>
```